One of Australia's fastest growing energy maintenance contractors needs a new website

www.panelbrite.com.au
Our business has evolved over the past years and now our website is no longer relevant.
We clean solar panels and we vacuum roof gutters.
We clean solar panels on the roofs of residential houses right up to billion dollar solar farms with in excess of 1 million panels. We offer thermal image testing and bird proofing for our residential and commercial clients and thermal drone imaging services for our solar farm clients.
We vacuum clean roof gutters (using a LoftSuk) on the residential house next door right up to enormous private and public schools, colleges, shopping centres, strat complexes and commercial buildings.
When first built our business had more of a domestic residential skew and the website reflected that. While that is still part of our core business we are now bidding on and have secured large government, commercial and infrastructure contracts and our new website needs to reflect our growth and our new business. We need a new site that it optimised for both desktop ad phone viewing as our latest figures showed that 73% of people visiting our site are on mobile phones. We have an extensive amount of data on Trekmetrics available as well as Bidlinks. Both that would also need integrating with the site along with a few other plugins such as Kembo Chat IQ, Friendwall etc along with SEO key words etc. We are also the winner and finalists over multiple years of the small business of the year awards and we like to proudly and prominently display those on our site.
We are looking for a new site with a modern professional feel / theme
There is a definitive break in our business between the solar Panel cleaning clients and the gutter cleaning clients so we would like a home page that begins with a simple choice:
Solar Panel Cleaning – Gutter Cleaning
With a professional full screen background image (we have hundreds to choose from) and along the bottom a small area with rights reserved etc, phone number etc (at some point in the future we will split these into two businesses but for now it’s what we have).
After that selection is made we would like a repeat of that same scenario but the selection is:
If it’s Solar Panel Cleaning
(new background image)
Government – Infrastructure – Commercial – Residential
If it’s Gutter Cleaning
(new background image)
Government – Strata – Commercial – Residential
After making those choices then onto the relevant pages with background images relevant to each sector and a them that suits (on the residential we would like to keep the link to our trekmetrics reviews) - We will provide copy / text for each relevant page.
Other than that, a menu inclusive of the above and:
Resellers Portal – we will provide a link to this from Kembo CRM)
Customer portal (we will supply a link to this from our booking system)
We also need a page for our Solar Resellers / Partners page but we will give them a link to this, it won’t be listed on the site.
Request a quote page (Again we will provide information from Kembo as this will be linked to the CRM)
Standard contact us page inclusive of phone numbers, address and fields supplied from CRM
Sydney – 02 7391 5084
Southern Highlands – 02 4863 1507
Goulburn – 02 4863 1507
Canberra – 02 6178 3045
Wollongong – 02 4239 7615
sales@panelbrite.com.au
Head Office - Ferndell NSW 2583
ABN: 48762093115
Responsive Design: Optimized for desktop and mobile (73% mobile visitors).
Fast Loading Speed: Optimized for performance.
Smooth Transition Animations: For service and category selection.
Sticky Contact Bar: Always accessible at the bottom of mobile screens for quick calls.
SEO Optimization: Focused on government tenders, large-scale commercial contracts, and infrastructure projects.
Integrations
Trekmetrics & Trekmetrics Bidlinks.
Kembo Chat IQ.
Friendwall Beacon.
SEO tools and keyword optimization.
Many many more images available if needed

```html
<!DOCTYPE html>
<html lang="en">
<head>
<meta charset="utf-8">
<title>Gutter Cleaning – Panel Brite</title>
<link href="https://fonts.googleapis.com/css2?family=Roboto:ital,wght@0,300;0,400;0,500;0,700;1,400;1,500&display=swap" rel="stylesheet">
<style>
:root{
  --blue:#0b63ae;
  --sky:#1fb0e6;
  --ink:#1b1b1b;
  --muted:#555;
  --grey-bg:#f4f4f4;
  --line:#d9d9d9;
  --star:#e8a32a;
  --footer:#141414;
  --white:#fff;
}
*{margin:0;padding:0;box-sizing:border-box}
html,body{width:1200px;height:3861px;overflow:hidden}
body{position:relative;font-family:"Roboto",sans-serif;color:var(--ink);background:var(--white)}
.abs{position:absolute}
.btn{position:absolute;display:flex;align-items:center;justify-content:center;gap:8px;height:36px;border-radius:18px;font-size:10.5px;font-weight:500;text-decoration:none}
.btn svg{width:16px;height:8px}
.btn-light{border:1.5px solid var(--white);color:var(--white)}
.btn-blue{border:1.5px solid var(--blue);color:var(--blue)}

/* nav */
.site-nav{left:0;top:0;width:1200px;height:62px;background:var(--white);z-index:3}
.nav-badge{left:0;top:0;z-index:4}
.brand{left:105px;top:20px;width:140px;text-align:center;z-index:5;color:var(--blue);font-weight:500;font-size:15px}
.brand-mark{display:block;width:22px;height:22px;margin:0 auto 6px;background:var(--blue)}
.nav-link{top:24px;font-size:10.5px;color:var(--ink);z-index:5}
.nav-link.active{color:var(--blue);font-style:italic;font-weight:500}
.nav-underline{left:721px;top:59px;width:38px;height:2px;background:var(--blue);z-index:5}
.nav-quote{left:957px;top:13px;width:137px;z-index:5}

/* hero */
.hero{left:0;top:62px;width:1200px;height:532px;background:linear-gradient(180deg,#6c7078 0%,#3f444d 45%,#2f3440 100%)}
.hero-shade{left:0;top:62px;width:1200px;height:532px;background:rgba(0,0,0,.25)}
.hero-title{left:0;top:245px;width:1200px;text-align:center;color:var(--white);font-size:55px;font-weight:400}
.hero-sub{left:200px;top:327px;width:800px;text-align:center;color:var(--white);font-size:24px;font-weight:300;line-height:33px}
.hero-btn{left:531px;top:426px;width:138px}

/* sectors */
.sectors{left:0;top:594px;width:1200px;height:525px;background:var(--blue)}
.sectors-title{left:0;top:670px;width:1200px;text-align:center;color:var(--white);font-size:24px;font-weight:400}
.sector-img{top:733px;width:182px;height:219px}
.sector-label{top:961px;width:182px;text-align:center;color:var(--white);font-size:12.5px;font-weight:500}
.sectors-btn{left:531px;top:1006px;width:138px}

/* reviews */
.reviews-title{left:0;top:1196px;width:1200px;text-align:center;font-size:39px;font-weight:400}
.rating{left:0;top:1258px;width:1200px;text-align:center;font-size:9px;color:var(--muted)}
.rating b{color:var(--blue);font-weight:500}
.rating .stars{color:var(--star);font-size:11px;letter-spacing:1px}
.review-card{top:1302px;width:250px;height:248px;background:var(--white);box-shadow:0 2px 8px rgba(0,0,0,.12);border-radius:3px;text-align:center}
.quote-dot{position:absolute;left:107px;top:20px;width:36px;height:36px;border-radius:50%;background:#ececec;color:var(--blue);font-size:22px;font-weight:700;line-height:42px}
.review-stars{position:absolute;left:0;top:62px;width:100%;color:var(--star);font-size:15px;letter-spacing:2px}
.review-text{position:absolute;left:18px;top:98px;width:214px;font-size:9.5px;line-height:15px;color:#444}
.review-name{position:absolute;left:0;top:201px;width:100%;font-size:11px;font-weight:500}
.review-verified{position:absolute;left:0;top:221px;width:100%;font-size:8px;color:#999}
.review-verified i{display:inline-block;width:8px;height:8px;border-radius:50%;background:var(--blue);margin-right:4px;vertical-align:-1px}
.arrow-btn{width:24px;height:24px;border:1.5px solid var(--blue);border-radius:50%;display:flex;align-items:center;justify-content:center}
.reviews-btn{left:531px;top:1582px;width:138px}

/* why */
.why{left:0;top:1690px;width:1200px;height:640px;background:var(--grey-bg)}
.why-frame{left:270px;top:1773px;width:279px;height:234px;border:1.5px solid var(--blue)}
.why-img{left:200px;top:1788px;width:331px;height:299px;background:linear-gradient(160deg,#5aa0d8 0%,#3f7a5a 45%,#2f3b3f 100%)}
.why-title{left:613px;top:1810px;font-size:39px;font-weight:400}
.why-item{font-size:12.5px;font-weight:500;display:flex;align-items:center;gap:8px}
.why-item svg{width:11px;height:11px}
.why-btn{left:613px;top:2002px;width:137px}

/* video */
.video{left:106px;top:2158px;width:988px;height:407px;background:linear-gradient(100deg,#5f7a3a 0%,#4a5a3a 40%,#3d5a8a 60%,#284a86 100%)}
.play{left:575px;top:2337px;width:50px;height:50px;border-radius:50%;background:var(--white);display:flex;align-items:center;justify-content:center}

/* explore */
.explore-title{left:0;top:2643px;width:1200px;text-align:center;font-size:38px;font-weight:400}
.acc-line{left:262px;width:676px;height:1px;background:var(--line)}
.acc-head{left:287px;font-size:22px;font-weight:400}
.acc-head.open{color:var(--blue);font-weight:500}
.acc-chev{left:889px}
.acc-text{left:287px;top:2855px;width:300px;font-size:9.5px;line-height:15px;color:#444}
.acc-text b{color:var(--blue);font-weight:500}
.acc-btn{left:287px;top:2972px;width:137px}
.acc-img{left:663px;top:2838px;width:250px;height:188px;background:linear-gradient(135deg,#3a3a3a 0%,#6a3b1c 45%,#d86a1a 60%,#3a2a20 100%)}

/* cta */
.cta{left:0;top:3170px;width:1200px;height:312px;background:var(--sky)}
.cta-img{left:0;top:3170px}
.cta-title{left:106px;top:3212px;width:520px;color:var(--white);font-size:38px;font-weight:400;line-height:54px}
.cta-btn{left:106px;top:3396px;width:137px}

/* footer */
.footer{left:0;top:3482px;width:1200px;height:379px;background:var(--footer)}
.f-brand{left:200px;top:3565px;width:190px;text-align:center;color:var(--white);font-size:31px;font-weight:500}
.f-brand span{display:block;width:54px;height:54px;margin:0 auto 14px;background:var(--sky)}
.f-head{font-size:13px;color:var(--white);font-weight:500;display:flex;align-items:center;gap:12px}
.f-head i{display:block;height:1px;background:#555}
.f-item{font-size:9.5px;color:#ddd;display:flex;align-items:center;gap:8px}
.f-item svg{width:9px;height:9px}
.f-item b{font-weight:500;color:var(--white)}
.f-link{font-size:10px;color:#ddd}
.social{width:30px;height:30px;border-radius:50%;background:#2c2c2c}
.f-copy{top:3798px;font-size:9px;color:#ddd}
.f-copy b{color:var(--white);font-weight:500}
</style>
</head>
<body>

<!-- navigation -->
<div class="abs site-nav"></div>
<svg class="abs nav-badge" width="260" height="135" viewBox="0 0 260 135"><path d="M105 60 H245 L182 124 Q175 131 168 124 Z" fill="#fff"/></svg>
<div class="abs brand"><span class="brand-mark"></span>Panel Brite</div>
<span class="abs nav-link" style="left:540px">Home</span>
<span class="abs nav-link" style="left:604px">Solar Cleaning</span>
<span class="abs nav-link active" style="left:704px">Gutter Cleaning</span>
<span class="abs nav-link" style="left:810px">LoftDust</span>
<span class="abs nav-link" style="left:878px">Contact us</span>
<div class="abs nav-underline"></div>
<a class="btn btn-blue nav-quote">Request a Quote <svg viewBox="0 0 16 8"><path d="M0 4H15M11 1L15 4L11 7" fill="none" stroke="currentColor"/></svg></a>

<!-- hero -->
<div class="abs hero" role="img" aria-label="Photo of a modern grey house with dark roof gutters"></div>
<div class="abs hero-shade"></div>
<h1 class="abs hero-title">Gutter Cleaning</h1>
<p class="abs hero-sub">Blocked gutters may appear insignificant, but ensuring their proper functioning brings numerous benefits to your home.</p>
<a class="btn btn-light hero-btn">Request a Quote <svg viewBox="0 0 16 8"><path d="M0 4H15M11 1L15 4L11 7" fill="none" stroke="currentColor"/></svg></a>

<!-- service sectors -->
<div class="abs sectors"></div>
<h2 class="abs sectors-title">Service sectors</h2>
<div class="abs sector-img" style="left:200px;background:linear-gradient(180deg,#4f8fd6,#c9c4b8 60%,#4f8a3a)" role="img" aria-label="Photo of a domed government building"></div>
<div class="abs sector-img" style="left:406px;background:linear-gradient(180deg,#cfd6dc,#8a7a5a 50%,#3f3a34)" role="img" aria-label="Photo of a strata apartment tower"></div>
<div class="abs sector-img" style="left:612px;background:linear-gradient(180deg,#7fa6cf,#3f5670 60%,#22303f)" role="img" aria-label="Photo of commercial glass skyscrapers"></div>
<div class="abs sector-img" style="left:818px;background:linear-gradient(180deg,#a9c6e0,#cfc8b8 50%,#5f8a4a)" role="img" aria-label="Photo of a residential house"></div>
<span class="abs sector-label" style="left:200px">Government</span>
<span class="abs sector-label" style="left:406px">Strata</span>
<span class="abs sector-label" style="left:612px">Commercial</span>
<span class="abs sector-label" style="left:818px">Residential</span>
<a class="btn btn-light sectors-btn">Request a Quote <svg viewBox="0 0 16 8"><path d="M0 4H15M11 1L15 4L11 7" fill="none" stroke="currentColor"/></svg></a>

<!-- reviews -->
<h2 class="abs reviews-title">We Love Happy Customers</h2>
<p class="abs rating"><b>Excellent:</b> &nbsp;<span class="stars">★★★★★</span> <b>4.9</b> based on &nbsp;<b>392</b> reviews</p>

<div class="abs arrow-btn" style="left:144px;top:1414px"><svg width="10" height="8" viewBox="0 0 10 8"><path d="M10 4H1M4 1L1 4L4 7" fill="none" stroke="#0b63ae"/></svg></div>
<div class="abs arrow-btn" style="left:1032px;top:1414px"><svg width="10" height="8" viewBox="0 0 10 8"><path d="M0 4H9M6 1L9 4L6 7" fill="none" stroke="#0b63ae"/></svg></div>

<div class="abs review-card" style="left:200px">
  <div class="quote-dot">”</div><div class="review-stars">★★★★★</div>
  <p class="review-text">Another excellent service from Panel Brite. arrived on time and completed the job well. easy to deal with and great technician.<br>we will have them again.</p>
  <p class="review-name">Callum Brevard</p><p class="review-verified"><i></i>Verified Customer</p>
</div>
<div class="abs review-card" style="left:475px">
  <div class="quote-dot">”</div><div class="review-stars">★★★★★</div>
  <p class="review-text">This is the third year the guys from Panel Brite have cleaned my gutters and i am very happy to recommend them. my job is not an easy one, double story with valleys and skylights in difficult places to access and the many before and after photos they attach to the...</p>
  <p class="review-name">Ned Farrow</p><p class="review-verified"><i></i>Verified Customer</p>
</div>
<div class="abs review-card" style="left:751px">
  <div class="quote-dot">”</div><div class="review-stars">★★★★★</div>
  <p class="review-text">Amazing job cleaning out my gutters.<br>it was sunny and very hot. definitely a lot more dirt in the gutters than i expected and a bit of extra work but no complaints from the cleaner. great work. would recommend to friends and family.</p>
  <p class="review-name">Tess K</p><p class="review-verified"><i></i>Verified Customer</p>
</div>
<a class="btn btn-blue reviews-btn">View all Review <svg viewBox="0 0 16 8"><path d="M0 4H15M11 1L15 4L11 7" fill="none" stroke="currentColor"/></svg></a>

<!-- why choose us -->
<div class="abs why"></div>
<div class="abs why-frame"></div>
<div class="abs why-img" role="img" aria-label="Photo of a worker pressure washing a roof gutter"></div>
<h2 class="abs why-title">Why Choose Us</h2>
<div class="abs why-item" style="left:615px;top:1888px"><svg viewBox="0 0 11 11"><path d="M5.5 0V11M0 5.5H11" stroke="#1fb0e6" stroke-width="1.6"/></svg>We don't climb on your roof</div>
<div class="abs why-item" style="left:615px;top:1920px"><svg viewBox="0 0 11 11"><path d="M5.5 0V11M0 5.5H11" stroke="#1fb0e6" stroke-width="1.6"/></svg>We don't scratch your gutters</div>
<div class="abs why-item" style="left:615px;top:1951px"><svg viewBox="0 0 11 11"><path d="M5.5 0V11M0 5.5H11" stroke="#1fb0e6" stroke-width="1.6"/></svg>We don't trash your gardens</div>
<div class="abs why-item" style="left:845px;top:1888px"><svg viewBox="0 0 11 11"><path d="M5.5 0V11M0 5.5H11" stroke="#1fb0e6" stroke-width="1.6"/></svg>No mess no fuss</div>
<div class="abs why-item" style="left:845px;top:1920px"><svg viewBox="0 0 11 11"><path d="M5.5 0V11M0 5.5H11" stroke="#1fb0e6" stroke-width="1.6"/></svg>Fixed price quotes</div>
<div class="abs why-item" style="left:845px;top:1951px"><svg viewBox="0 0 11 11"><path d="M5.5 0V11M0 5.5H11" stroke="#1fb0e6" stroke-width="1.6"/></svg>No leaf left behind!</div>
<a class="btn btn-blue why-btn">Request a Quote <svg viewBox="0 0 16 8"><path d="M0 4H15M11 1L15 4L11 7" fill="none" stroke="currentColor"/></svg></a>

<!-- video -->
<div class="abs video" role="img" aria-label="Video still of a gutter vacuum hose over a blue corrugated roof"></div>
<div class="abs play"><svg width="22" height="22" viewBox="0 0 22 22"><circle cx="11" cy="11" r="11" fill="#0b63ae"/><path d="M9 7L15 11L9 15Z" fill="#fff"/></svg></div>

<!-- explore -->
<h2 class="abs explore-title">Explore Gutter Cleaning</h2>
<div class="abs acc-line" style="top:2724px"></div>
<span class="abs acc-head" style="top:2733px">Gutter Cleaning</span>
<svg class="abs acc-chev" style="top:2743px" width="20" height="8" viewBox="0 0 20 8"><path d="M1 1L10 6L19 1" fill="none" stroke="#1fb0e6" stroke-width="2"/></svg>
<div class="abs acc-line" style="top:2774px"></div>
<span class="abs acc-head open" style="top:2783px">Bushfire Preparation</span>
<svg class="abs acc-chev" style="top:2794px" width="20" height="8" viewBox="0 0 20 8"><path d="M1 7L10 2L19 7" fill="none" stroke="#0b63ae" stroke-width="2"/></svg>
<p class="abs acc-text">Pine needles, leaves, twigs, and other dry debris lying in a gutter can easily serve as fuel for a fire caused by a few floating embers. these embers not only can drift up to a kilometre from a fire, but they are also more apt to ignite in the semi-enclosed area of a gutter. that's why it is pivotal for homeowners to keep their gutters clean during the hot and dry seasons ... <b>[More]</b></p>
<a class="btn btn-blue acc-btn">Request a Quote <svg viewBox="0 0 16 8"><path d="M0 4H15M11 1L15 4L11 7" fill="none" stroke="currentColor"/></svg></a>
<div class="abs acc-img" role="img" aria-label="Photo of embers burning in dry leaves inside a gutter"></div>
<div class="abs acc-line" style="top:3045px"></div>
<span class="abs acc-head" style="top:3054px">Complete Service</span>
<svg class="abs acc-chev" style="top:3064px" width="20" height="8" viewBox="0 0 20 8"><path d="M1 1L10 6L19 1" fill="none" stroke="#1fb0e6" stroke-width="2"/></svg>
<div class="abs acc-line" style="top:3095px"></div>

<!-- call to action -->
<div class="abs cta"></div>
<svg class="abs cta-img" width="1200" height="312" viewBox="0 0 1200 312" role="img" aria-label="Photo of a dark house roof edge with gutters and downpipe">
  <defs><linearGradient id="roofTone" x1="0" y1="0" x2="1" y2="1"><stop offset="0" stop-color="#3a4150"/><stop offset=".6" stop-color="#23293a"/><stop offset="1" stop-color="#4a5060"/></linearGradient></defs>
  <path d="M712 0H1200V312H630Z" fill="url(#roofTone)"/>
</svg>
<h2 class="abs cta-title">Get the full treatment and have peace of mind this summer season</h2>
<a class="btn btn-light cta-btn">Request a Quote <svg viewBox="0 0 16 8"><path d="M0 4H15M11 1L15 4L11 7" fill="none" stroke="currentColor"/></svg></a>

<!-- footer -->
<div class="abs footer"></div>
<div class="abs f-brand"><span></span>Panel Brite</div>

<div class="abs f-head" style="left:469px;top:3559px;width:182px">Contact us<i style="flex:1"></i></div>
<div class="abs f-item" style="left:469px;top:3590px"><svg viewBox="0 0 9 9"><path d="M4.5 0A3 3 0 0 1 7.5 3C7.5 5 4.5 9 4.5 9S1.5 5 1.5 3A3 3 0 0 1 4.5 0Z" fill="#1fb0e6"/></svg><span><b>Head Office</b> - Ferndell NSW 2583</span></div>
<div class="abs f-item" style="left:469px;top:3615px"><svg viewBox="0 0 9 9"><rect x="0" y="1.5" width="9" height="6" fill="#1fb0e6"/><path d="M0 1.5L4.5 5L9 1.5" fill="none" stroke="#141414"/></svg>sales@panelbrite.com.au</div>
<div class="abs f-item" style="left:469px;top:3640px"><svg viewBox="0 0 9 9"><path d="M1 1L3 0.5L4 3L3 4Q4 6 5.5 6.5L6.5 5.5L9 6.5L8.5 8.5Q3 8.5 0.5 2Z" fill="#1fb0e6"/></svg><span><b>Sydney</b> - 02 7391 5084</span></div>
<div class="abs f-item" style="left:469px;top:3665px"><svg viewBox="0 0 9 9"><path d="M1 1L3 0.5L4 3L3 4Q4 6 5.5 6.5L6.5 5.5L9 6.5L8.5 8.5Q3 8.5 0.5 2Z" fill="#1fb0e6"/></svg><span><b>Southern Highlands</b> - 02 4863 1507</span></div>
<div class="abs f-item" style="left:469px;top:3690px"><svg viewBox="0 0 9 9"><path d="M1 1L3 0.5L4 3L3 4Q4 6 5.5 6.5L6.5 5.5L9 6.5L8.5 8.5Q3 8.5 0.5 2Z" fill="#1fb0e6"/></svg><span><b>Goulburn</b> - 02 4863 1507</span></div>
<div class="abs f-item" style="left:469px;top:3715px"><svg viewBox="0 0 9 9"><path d="M1 1L3 0.5L4 3L3 4Q4 6 5.5 6.5L6.5 5.5L9 6.5L8.5 8.5Q3 8.5 0.5 2Z" fill="#1fb0e6"/></svg><span><b>Canberra</b> - 02 6178 3045</span></div>
<div class="abs f-item" style="left:469px;top:3740px"><svg viewBox="0 0 9 9"><path d="M1 1L3 0.5L4 3L3 4Q4 6 5.5 6.5L6.5 5.5L9 6.5L8.5 8.5Q3 8.5 0.5 2Z" fill="#1fb0e6"/></svg><span><b>Wollongong</b> - 02 4239 7615</span></div>

<div class="abs f-head" style="left:732px;top:3559px;width:181px">Quick links<i style="flex:1"></i></div>
<span class="abs f-link" style="left:732px;top:3593px">Home</span>
<span class="abs f-link" style="left:732px;top:3618px">Solar Cleaning</span>
<span class="abs f-link" style="left:732px;top:3643px">Gutter Cleaning</span>
<span class="abs f-link" style="left:732px;top:3668px">LoftDust</span>
<span class="abs f-link" style="left:732px;top:3693px">Contact us</span>
<span class="abs f-link" style="left:732px;top:3718px">Terms and conditions</span>
<span class="abs f-link" style="left:732px;top:3743px">Privacy policy</span>

<div class="abs social" style="left:970px;top:3567px"></div>
<div class="abs social" style="left:970px;top:3605px"></div>
<div class="abs social" style="left:970px;top:3642px"></div>
<div class="abs social" style="left:970px;top:3680px"></div>

<p class="abs f-copy" style="left:200px">© 2025 <b>Panel Brite.</b> All Right Reserved</p>
<p class="abs f-copy" style="left:469px"><b>ABN:</b> 48762093115</p>
<svg class="abs" style="left:1088px;top:3796px" width="14" height="14" viewBox="0 0 14 14"><path d="M7 0L13 14L7 10L1 14Z" fill="#1fb0e6"/></svg>

</body>
</html>
```